Wordpress Website for electrician

I'm looking for an easy to maintain website for my electrical contracting business. Need a professional and appealing site.
Im wanting a website where clients can come on and look at services we offer, case studies and advertise our services.
Colours I'm wanting to incorporate are green, white, black and grey
I'm wanting a big slide show on main page where I can place advertising etc.
Menu is to include home, services, our work, specials, energy efficiency and contact
My existing site is www.trelwirefix.com.au
Updates
looking for something with a similar layout to this website
Target Market(s)
Businesses
Industry/Entity Type
Electrician
Look and feel

```html
<!DOCTYPE html>
<html lang="en">
<head>
<meta charset="utf-8">
<title>Trelwirefix – Electrical Contractor</title>
<link rel="stylesheet" href="https://fonts.googleapis.com/css2?family=Roboto:wght@300;400;500;700&display=swap">
<style>
:root{
  --green:#84b95c;
  --green-dark:#4e9a2b;
  --green-text:#5aae3a;
  --dark:#3b3b3b;
  --grey-bg:#f1f1f1;
  --grey-line:#dcdcdc;
  --text:#555;
  --white:#fff;
}
*{margin:0;padding:0;box-sizing:border-box}
html,body{width:1200px;height:2197px;overflow:hidden}
body{font-family:'Roboto',Arial,sans-serif;color:var(--text);background:var(--white);position:relative}
.abs{position:absolute}
.topbar{left:0;top:0;width:1200px;height:32px;background:var(--dark);color:#ddd;font-size:11px}
.topbar .item{position:absolute;top:10px;display:flex;align-items:center;gap:12px}
.header{left:0;top:32px;width:1200px;height:90px;background:#fafafa}
.brand{position:absolute;left:115px;top:22px;display:flex;align-items:center;gap:10px;font-size:30px;font-weight:500;color:var(--green-dark)}
.brand .dot{width:22px;height:22px;border-radius:50%;background:var(--green-dark)}
.nav a{position:absolute;top:45px;height:45px;display:flex;align-items:center;font-size:14.5px;color:#222;text-decoration:none;text-transform:uppercase}
.nav a.active{background:var(--green-dark);color:var(--white);justify-content:center}
.hero{left:0;top:122px;width:1200px;height:486px;background:var(--green);overflow:hidden}
.hero-line{position:absolute;left:108px;color:var(--white);text-transform:uppercase;white-space:nowrap;line-height:1}
.hero-line.l1{top:72px;font-size:63px;font-weight:500}
.hero-line.l2{top:138px;font-size:55px;font-weight:300}
.hero-line.l3{top:198px;font-size:52px;font-weight:300}
.hero-line.l3 b{font-weight:700;font-size:48px}
.hero-line.l4{top:256px;font-size:48px;font-weight:700}
.hero-photo{position:absolute;left:530px;top:200px;width:616px;height:286px;background:radial-gradient(ellipse at 50% 75%,#f4c98e 0%,#e7b57a 35%,#b9cf8a 75%,var(--green) 100%);border-radius:140px 140px 0 0}
.intro{left:149px;top:636px;width:900px;font-size:15px;line-height:17px;font-weight:300;color:#555}
.intro strong{font-size:27px;font-weight:400;color:var(--green-dark)}
.divider{left:104px;top:733px;width:992px;height:1px;background:var(--grey-line)}
.feature h2{font-size:24px;font-weight:300;color:var(--green-text);line-height:23px;margin-bottom:12px}
.feature p{font-size:13.5px;line-height:19.5px;font-weight:300;color:#555}
.works{left:0;top:1133px;width:1200px;height:379px;background:var(--grey-bg);border-top:3px solid #e2e2e2;border-bottom:3px solid #e2e2e2}
.works h2{position:absolute;left:106px;top:34px;font-size:24px;font-weight:300;color:var(--green-text)}
.arrows{position:absolute;left:1046px;top:42px;display:flex;gap:4px}
.arrows span{width:20px;height:20px;background:#aaa;border-radius:3px;display:flex;align-items:center;justify-content:center}
.card{position:absolute;top:83px;width:232px;height:229px;background:var(--white);box-shadow:0 1px 4px rgba(0,0,0,.2)}
.card .img{height:146px;border-bottom:3px solid var(--green)}
.card h3{text-align:center;font-size:17px;font-weight:400;color:#444;margin-top:14px}
.card p{text-align:center;font-size:10px;color:#999;margin-top:8px;text-transform:uppercase}
.service{top:1566px;width:304px;height:288px;background:var(--green);padding:5px}
.service .inner{border:2px solid rgba(255,255,255,.55);height:100%;text-align:center;color:var(--white);padding:18px 18px 0}
.service h3{font-size:31px;font-weight:400;line-height:32px;text-transform:uppercase;margin-bottom:20px}
.service p{font-size:14px;line-height:20px;font-weight:300;height:132px}
.service a{color:#1e1e1e;font-size:15px;text-decoration:none}
.footer{left:0;top:1915px;width:1200px;height:282px;background:var(--dark);border-top:4px solid var(--green)}
.fbrand{position:absolute;left:104px;top:22px;font-size:30px;font-weight:500;color:#111;display:flex;align-items:center;gap:10px}
.fbrand .dot{width:22px;height:22px;border-radius:50%;background:#111}
.mail{position:absolute;left:104px;top:92px;font-size:14px;color:#ccc}
.social{position:absolute;left:104px;top:134px;display:flex;gap:11px}
.social span{width:32px;height:32px;border-radius:50%;background:#6a6a6a}
.testi-title{position:absolute;left:442px;top:30px;font-size:26px;font-weight:300;color:var(--green)}
.quote{position:absolute;left:445px;top:88px;width:307px;height:96px;border:2px solid var(--green);padding:4px}
.quote div{background:var(--green);height:100%;color:var(--white);font-size:14px;line-height:20px;padding:16px 14px 0 28px}
.testi-more{position:absolute;left:446px;top:200px;font-size:14px;color:var(--green)}
.badge{position:absolute;left:832px;top:22px;width:264px;height:176px;background:#4c5660;border-radius:10px}
.fphone{position:absolute;left:833px;top:208px;font-size:38px;line-height:44px;font-weight:500;color:#cfcfcf}
</style>
</head>
<body>
<div class="abs topbar">
  <div class="item" style="left:117px">
    <svg width="12" height="12" viewBox="0 0 24 24"><path fill="#ddd" d="M6.6 10.8a15 15 0 0 0 6.6 6.6l2.2-2.2c.3-.3.7-.4 1-.2 1.1.4 2.3.6 3.6.6.6 0 1 .4 1 1V20c0 .6-.4 1-1 1A17 17 0 0 1 3 4c0-.6.4-1 1-1h3.5c.6 0 1 .4 1 1 0 1.2.2 2.4.6 3.6.1.3 0 .7-.2 1z"/></svg>
    <span>0400 555 018</span>
  </div>
  <div class="item" style="left:285px">
    <svg width="14" height="11" viewBox="0 0 14 11"><rect width="14" height="11" rx="1" fill="#ddd"/><path d="M0 1l7 5 7-5" stroke="#3b3b3b" fill="none"/></svg>
    <span>info@trelwirefix.com.au</span>
  </div>
</div>

<header class="abs header">
  <div class="brand"><span class="dot"></span>trelwirefix</div>
  <nav class="nav">
    <a class="active" href="#" style="left:467px;width:79px">Home</a>
    <a href="#" style="left:558px">Services</a>
    <a href="#" style="left:659px">Our Work</a>
    <a href="#" style="left:768px">Specials</a>
    <a href="#" style="left:867px">Energy Efficiency</a>
    <a href="#" style="left:1045px">Contact</a>
  </nav>
</header>

<section class="abs hero">
  <div class="hero-photo" role="img" aria-label="Smiling family of four with their pet cat"></div>
  <h1>
    <span class="hero-line l1">Reduce your electric</span>
    <span class="hero-line l2">Bills by lowering</span>
    <span class="hero-line l3">Your&nbsp; <b>energy</b></span>
    <span class="hero-line l4">Consumption</span>
  </h1>
</section>

<p class="abs intro">At <strong>Trelwirefix</strong> we want what is best for you and the environment. Every job we approach we try to incorparate energy efficiency into them. If its going to help you save money or lower the impact on the environment then we will encourage it when discussing work with you.</p>
<div class="abs divider"></div>

<div class="abs feature" style="left:104px;top:770px;width:380px">
  <h2>Led Is The Future</h2>
  <p>LED lighting has involved rapidly in the last 5 years. In the coming years we will see all lighting being substitued with LED lights. It is by far the most efficient form of lighting on todays market. Let us retrofit your business or home with LED and the savings will literally pay the lights off.</p>
</div>
<div class="abs" style="left:501px;top:797px;width:60px;height:122px;border-radius:8px;background:radial-gradient(circle at 50% 35%,#fff,#ddd 60%,#999)" role="img" aria-label="LED light bulb"></div>

<div class="abs feature" style="left:621px;top:770px;width:360px">
  <h2>Reduce Your Business<br>Energy Consumption</h2>
  <p>By letting us analyse your energy consumption, we can identify where you are simply burning your money. We can suggest and implement easy solutions to save you money and minimise your carbon emmissions.</p>
</div>
<div class="abs" style="left:1018px;top:795px;width:62px;height:120px;border-radius:8px;background:radial-gradient(circle at 50% 60%,#c7e15a,#5aa02a 70%,transparent 72%)" role="img" aria-label="Seedling growing from a globe"></div>

<div class="abs feature" style="left:104px;top:946px;width:362px">
  <h2>News</h2>
  <p>Kestrowatt Bulletin Household demand: Why rooftop solar keeps reshaping the evening peak Kestrowatt Bulletin One of the steady trends in the energy business used to be the regular year-in, year-out rise in...</p>
</div>
<div class="abs" style="left:482px;top:992px;width:102px;height:90px;background:linear-gradient(#5aa0e0,#1e5ca8);border-radius:14px" role="img" aria-label="News app icon"></div>

<div class="abs feature" style="left:621px;top:946px;width:362px">
  <h2>Special</h2>
  <p>Beat the heat this summer and install a brand new split system airconditioner. We will supply and install a brand new Kelvara KV-25S 2.5kW split system airconditoner. This new look airconditioner has a cooling capacity of 2.5kW and a heating capacity of 3.3kW.</p>
</div>
<div class="abs" style="left:998px;top:982px;width:106px;height:112px;background:linear-gradient(135deg,#7cc23c,#3a8a1c);border-radius:4px" role="img" aria-label="Wrapped gift box"></div>

<section class="abs works">
  <h2>Recent Works</h2>
  <div class="arrows">
    <span><svg width="8" height="8" viewBox="0 0 8 8"><path d="M5.5 1L2.5 4l3 3" stroke="#fff" fill="none" stroke-width="1.5"/></svg></span>
    <span><svg width="8" height="8" viewBox="0 0 8 8"><path d="M2.5 1l3 3-3 3" stroke="#fff" fill="none" stroke-width="1.5"/></svg></span>
  </div>
  <div class="card" style="left:106px"><div class="img" style="background:linear-gradient(#c9b8a4,#7a6048)" role="img" aria-label="Industrial cable trays"></div><h3>Industrial</h3><p>Some description here</p></div>
  <div class="card" style="left:357px"><div class="img" style="background:linear-gradient(#4b6a8a,#b8aa90)" role="img" aria-label="Commercial boardroom fit-out"></div><h3>Commercial</h3><p>Some description here</p></div>
  <div class="card" style="left:610px"><div class="img" style="background:linear-gradient(#e6e2dc,#b9a796)" role="img" aria-label="Domestic air conditioner unit"></div><h3>Domestic</h3><p>Some description here</p></div>
  <div class="card" style="left:861px"><div class="img" style="background:linear-gradient(#9cc3e6,#3d5f8c 55%,#b86d3e)" role="img" aria-label="Solar panels on a tiled roof"></div><h3>Solar</h3><p>Some description here</p></div>
</section>

<div class="abs service" style="left:104px"><div class="inner"><h3>Electrical<br>Contracting</h3><p>We offer all types of electrical work from Installation to maintenance. With experience in all aspects of the industry.Industrial, commercial and domestic. Installation, maintenance and breakdown call outs.</p><a href="#">Know More ...</a></div></div>
<div class="abs service" style="left:447px"><div class="inner"><h3>Energy<br>Efficiency</h3><p>An energy efficient audit can identify issues of innefficiency in your business or home. We can implement our solutions and save money on energy bills and substantially decrease your carbon footprint.</p><a href="#">Know More ...</a></div></div>
<div class="abs service" style="left:790px"><div class="inner"><h3>Underground<br>Locating</h3><p>With the use of radiowaves we can induce a signal into conductive materials underground, making it easier to find a lot of services such as cables and pipes.</p><a href="#">Know More ...</a></div></div>

<footer class="abs footer">
  <div class="fbrand"><span class="dot"></span>trelwirefix</div>
  <div class="mail">sales@trelwirefix.com.au</div>
  <div class="social"><span></span><span></span><span></span></div>
  <h2 class="testi-title">Testimonials</h2>
  <svg class="abs" style="left:456px;top:66px" width="26" height="24" viewBox="0 0 26 24"><path d="M0 0l26 24H6z" fill="var(--green)"/></svg>
  <div class="quote"><div>Trelwirefix considerd all our needs and incorparated energy saving into the project...</div></div>
  <div class="testi-more">Know More ...</div>
  <div class="badge" role="img" aria-label="Accreditation badge"></div>
  <div class="fphone">0400-555-018</div>
</footer>
</body>
</html>
```